Drowsy Heron

Need a business card for our restaurant. Restaurant and Bar in the mountains of North Idaho. Rustic looking card

Contact Information for Business Card

rustic design, wood and metal looking, primarily neutral colors

Requirements
Must have
• Name, address, phone number, website, email address

```html
<!DOCTYPE html>
<html lang="en">
<head>
<meta charset="utf-8">
<title>Drowsy Heron — Business Card</title>
<link href="https://fonts.googleapis.com/css2?family=Lato:wght@400&family=Permanent+Marker&display=swap" rel="stylesheet">
<style>
  :root {
    --backdrop: #d8d3cc;
    --card: #000000;
    --ink: #ffffff;
    --ink-soft: #e6e6e6;
    --illustration: #cfcfcf;
  }
  * { margin: 0; padding: 0; box-sizing: border-box; }
  html, body {
    width: 1047px;
    height: 1200px;
    overflow: hidden;
    background: var(--backdrop);
  }
  .canvas {
    position: relative;
    width: 1047px;
    height: 1200px;
  }
  .card {
    position: absolute;
    left: 156px;
    width: 743px;
    height: 424px;
    background: var(--card);
    color: var(--ink);
    font-family: "Lato", sans-serif;
    overflow: hidden;
  }
  .card--front { top: 120px; }
  .card--back { top: 634px; }

  .band {
    position: absolute;
    left: 0;
    width: 100%;
    height: 9px;
    background: var(--ink);
  }
  .band--top { top: 0; }
  .band--bottom { bottom: 0; }

  .mascot-art {
    position: absolute;
    left: 481px;
    top: 9px;
    width: 236px;
    height: 215px;
    background: radial-gradient(ellipse at 50% 55%, var(--illustration) 0%, #8a8a8a 55%, var(--card) 100%);
    border-radius: 4px;
  }

  .person-name {
    position: absolute;
    left: 52px;
    top: 180px;
    font-family: "Permanent Marker", cursive;
    font-weight: 400;
    font-size: 34px;
    line-height: 40px;
    letter-spacing: 1px;
    color: var(--ink-soft);
    white-space: nowrap;
  }
  .person-title {
    position: absolute;
    left: 52px;
    top: 226px;
    font-size: 21px;
    line-height: 26px;
    white-space: nowrap;
  }
  .contact-list {
    position: absolute;
    left: 52px;
    top: 275px;
    list-style: none;
  }
  .contact-item {
    display: flex;
    align-items: center;
    height: 26px;
    font-size: 16.5px;
    white-space: nowrap;
  }
  .contact-icon {
    width: 13px;
    height: 13px;
    margin-right: 12px;
    fill: var(--ink);
    flex: none;
  }

  .brand-lockup {
    position: absolute;
    inset: 0;
    display: flex;
    align-items: center;
    justify-content: center;
    gap: 16px;
  }
  .brand-dot {
    width: 22px;
    height: 22px;
    border-radius: 50%;
    background: var(--ink);
  }
  .brand-name {
    font-family: "Lato", sans-serif;
    font-weight: 400;
    font-size: 34px;
    letter-spacing: 4px;
    text-transform: uppercase;
    color: var(--ink);
    white-space: nowrap;
  }
</style>
</head>
<body>
<main class="canvas">

  <section class="card card--front">
    <div class="band band--top"></div>
    <div class="mascot-art" role="img" aria-label="Illustration of the restaurant's mascot animal hanging upside down"></div>

    <h1 class="person-name">MARK ELLISON</h1>
    <p class="person-title">Founder &amp; CEO</p>

    <ul class="contact-list">
      <li class="contact-item">
        <svg class="contact-icon" viewBox="0 0 24 24" aria-hidden="true"><path d="M6.6 10.8a15.1 15.1 0 0 0 6.6 6.6l2.2-2.2c.3-.3.7-.4 1-.2 1.1.4 2.3.6 3.6.6.6 0 1 .4 1 1V20c0 .6-.4 1-1 1C10.6 21 3 13.4 3 4c0-.6.4-1 1-1h3.5c.6 0 1 .4 1 1 0 1.3.2 2.5.6 3.6.1.3 0 .7-.2 1z"/></svg>
        (555) 312-0147
      </li>
      <li class="contact-item">
        <svg class="contact-icon" viewBox="0 0 24 24" aria-hidden="true"><path d="M2 5h20v14H2z"/><path d="M3 6l9 7 9-7" stroke="#000" stroke-width="1.6" fill="none"/></svg>
        info@thedrowsyheronlarkspur.com
      </li>
      <li class="contact-item">
        <svg class="contact-icon" viewBox="0 0 24 24" aria-hidden="true"><circle cx="12" cy="12" r="10"/><path d="M2 12h20M12 2c3 3 3 17 0 20M12 2c-3 3-3 17 0 20" stroke="#000" stroke-width="1.6" fill="none"/></svg>
        thedrowsyheronlarkspur.com
      </li>
      <li class="contact-item">
        <svg class="contact-icon" viewBox="0 0 24 24" aria-hidden="true"><path d="M12 2a7 7 0 0 0-7 7c0 5.2 7 13 7 13s7-7.8 7-13a7 7 0 0 0-7-7zm0 9.5a2.5 2.5 0 1 1 0-5 2.5 2.5 0 0 1 0 5z"/></svg>
        238 Cedar St, Larkspur, ID 83999
      </li>
    </ul>

    <div class="band band--bottom"></div>
  </section>

  <section class="card card--back">
    <div class="brand-lockup">
      <span class="brand-dot"></span>
      <span class="brand-name">Drowsy Heron</span>
    </div>
  </section>

</main>
</body>
</html>
```